Lakeshore Freightways Council Web Update

Update wordpress based association web site. Please look up www.lakeshorefreightwayscouncil.com for our web site to get a feel for what we currently having. We would like our updated web site to look similar to: www.brightoakfund.com. We will provide our key points for updating in a future email.

Target Market(s)

duplicate the brightoakfund.com format please.

Number of Pages Required

4 page

Font styles to use
Serif

Requirements
Must have
• duplicate the brightoakfund.com format please. You will keep most of the content that we currently have on our website.
Nice to have
• n/a
Should not have
• n/a

```html
<!DOCTYPE html>
<html lang="en">
<head>
<meta charset="utf-8">
<title>Lakeshore Freightways Council</title>
<link rel="stylesheet" href="https://fonts.googleapis.com/css2?family=Raleway:wght@400;500;600;700&display=swap">
<style>
:root{
  --navy:#1c1d7c;
  --navy-deep:#16176a;
  --bar:#3a3b9c;
  --orange:#f08a4b;
  --ink:#444;
  --muted:#666;
  --panel:rgba(244,244,247,.93);
  --line:#cfd0d6;
  --white:#fff;
}
*{box-sizing:border-box;margin:0;padding:0}
html,body{width:1200px;height:3448px;overflow:hidden}
body{font-family:"Raleway",sans-serif;color:var(--ink);background:var(--white);position:relative}
.abs{position:absolute}
/* header */
.site-header{left:0;top:0;width:1200px;height:115px;background:var(--white)}
.brand{left:85px;top:18px;width:150px;font-weight:700;font-size:17px;line-height:19px;color:var(--navy);border-bottom:2px solid var(--navy);padding-bottom:6px}
.contact-strip{left:282px;top:14px;font-size:13px;color:var(--muted);display:flex;gap:26px}
.contact-strip span::before{content:"";display:inline-block;width:8px;height:8px;border-radius:50%;background:var(--orange);margin-right:6px;vertical-align:1px}
.header-rule{left:282px;top:42px;width:832px;height:1px;background:var(--line)}
.menu{left:858px;top:70px;font-size:15px;color:var(--navy);display:flex;align-items:center;gap:8px}
.menu i{display:block;width:20px;height:3px;background:var(--navy);box-shadow:0 6px 0 var(--navy),0 -6px 0 var(--navy)}
.search{left:960px;top:66px;width:155px;height:24px;border-bottom:1px solid var(--navy)}
.search svg{position:absolute;right:2px;top:4px}
/* hero */
.hero{left:0;top:115px;width:1200px;height:556px;background:linear-gradient(160deg,#5c6a4a 0%,#3f4b35 35%,#7a6a3a 60%,#c78a25 75%,#4a4e40 100%)}
.hero-caption{left:368px;top:340px;width:460px;height:120px;background:rgba(255,255,255,.92);border-bottom:4px solid var(--orange);font-size:15px;line-height:26px;text-align:center;padding:18px 22px;color:#333}
.slider-arrow{top:357px;width:58px;height:58px;border-radius:50%;background:rgba(255,255,255,.45)}
.slider-arrow svg{position:absolute;left:17px;top:17px}
/* welcome */
.portrait{left:85px;top:662px;width:212px;height:239px;background:linear-gradient(180deg,#8a6a5c,#4a3a3a)}
.portrait-name{left:85px;top:866px;width:212px;height:35px;background:var(--orange);color:var(--white);font-size:14px;font-weight:600;text-align:center;line-height:35px}
.portrait-name em{font-style:normal;font-weight:400;color:#ffe;margin-left:4px}
.welcome-title{left:329px;top:736px;font-size:24px;font-weight:500;color:var(--orange)}
.welcome-text{left:329px;top:780px;width:790px;font-size:13.5px;line-height:25px;color:var(--muted)}
/* feature rows */
.feature-photo{left:0;width:1200px}
.feature-panel{background:var(--panel);padding:60px 30px 0 30px}
.feature-panel h2{font-size:31px;font-weight:600;color:var(--navy);margin-bottom:26px}
.feature-panel p{font-size:13.5px;line-height:25px;color:#555;margin-bottom:22px}
.btn{display:inline-block;border:1px solid var(--navy);color:var(--navy);border-radius:6px;font-size:13px;padding:10px 20px;margin-top:6px}
/* newsletter */
.newsletter-bg{left:0;top:2580px;width:1200px;height:278px;background:linear-gradient(90deg,#1a1f3a,#2d3350 50%,#1c2038)}
.newsletter-box{left:85px;top:2621px;width:1030px;height:189px;background:var(--panel);padding:30px 30px 0}
.newsletter-box h2{font-size:31px;font-weight:600;color:var(--navy)}
.field{top:101px;height:46px;border:1px solid #c9c9cf;background:#fafafa;font-size:13px;color:#888;padding:14px 14px}
.send{left:878px;top:101px;width:115px;height:46px;background:var(--orange);color:var(--white);font-size:17px;border-radius:3px;display:flex;align-items:center;justify-content:center;gap:8px}
/* contacts */
.contact-item{top:2917px;width:260px;text-align:center}
.contact-icon{width:74px;height:74px;border:2px solid var(--orange);border-radius:50%;margin:0 auto 24px;position:relative}
.contact-icon svg{position:absolute;left:19px;top:19px}
.contact-item p{font-size:15px;line-height:22px;color:#333;font-weight:500}
.contact-item p.big{font-size:20px}
/* footer */
.about{left:0;top:3108px;width:1200px;height:294px;background:var(--navy-deep)}
.about h2{position:absolute;left:85px;top:26px;font-size:25px;font-weight:600;color:var(--white)}
.about-text{left:85px;top:70px;width:525px;font-size:12.5px;line-height:23px;color:#e6e6f2}
.badge{left:651px;top:32px;width:181px;height:230px;background:var(--white);padding:8px}
.badge-shape{width:165px;height:170px;background:linear-gradient(180deg,#1c1d7c 0 55%,#c23a3a 55% 70%,#1c1d7c 70%)}
.badge p{font-size:11px;font-style:normal;text-align:center;color:var(--navy);margin-top:10px;line-height:15px}
.feed{left:890px;top:32px;width:223px;height:230px;background:var(--white);padding:10px;font-size:11px;color:#333}
.feed h3{font-size:14px;font-weight:700;border-bottom:1px solid #ddd;padding-bottom:8px;margin-bottom:12px}
.feed .av{display:inline-block;width:26px;height:26px;background:#d87a3a;border-radius:50%;vertical-align:top;margin-right:6px}
.legal{left:0;top:3402px;width:1200px;height:46px;background:var(--bar);color:#d8d8f0;font-size:12px;padding:16px 85px}
</style>
</head>
<body>

<header class="abs site-header">
  <div class="abs brand">Lakeshore Freightways Council</div>
  <div class="abs contact-strip">
    <span>410 Harbor Street, Suite 220 Marlow, MI 49001</span>
    <span>(555) 014-2210</span>
    <span>(555) 014-2288</span>
    <span>info@lakeshorefreightwayscouncil.com</span>
  </div>
  <div class="abs header-rule"></div>
  <div class="abs menu">Menu <i></i></div>
  <div class="abs search"><svg width="14" height="14" viewBox="0 0 14 14"><circle cx="6" cy="6" r="4.5" fill="none" stroke="#1c1d7c" stroke-width="2"/><line x1="9" y1="9" x2="13" y2="13" stroke="#1c1d7c" stroke-width="2"/></svg></div>
</header>

<section class="abs hero" role="img" aria-label="Orange freight locomotive leading a train through green trees">
</section>
<div class="abs slider-arrow" style="left:17px"><svg width="24" height="24" viewBox="0 0 24 24"><path d="M15 4 L7 12 L15 20" fill="none" stroke="#fff" stroke-width="3"/></svg></div>
<div class="abs slider-arrow" style="left:1125px"><svg width="24" height="24" viewBox="0 0 24 24"><path d="M9 4 L17 12 L9 20" fill="none" stroke="#fff" stroke-width="3"/></svg></div>
<div class="abs hero-caption">From 1980 to 2012, the train accident rate fell 80 percent, the rail employee injury rate fell 85 percent and the grade crossing collision rate fell 82 percent.</div>

<section class="welcome">
  <div class="abs portrait" role="img" aria-label="Portrait of the council president"></div>
  <div class="abs portrait-name">Dale Whitcomb <em>(President)</em></div>
  <h2 class="abs welcome-title">Welcome</h2>
  <p class="abs welcome-text">I would like to welcome you to the Lakeshore Freightways Council website. Here you will find valuable information on Michigan railroads, including issues and concerns in and around the railroad industry. We are an active and aggressive state railroad association and we look forward to continued success with our partnerships. Please make sure to click on our member railroad company links while you're here. Also, sign up for our newsletter and follow the LFC on our news feed. Thank you and I hope you enjoy your visit to our website.</p>
</section>

<section>
  <div class="abs feature-photo" style="top:936px;height:512px;background:linear-gradient(120deg,#0d1a2e,#1d3458 45%,#6a86a8 80%,#dfe7f0)" role="img" aria-label="Dark freight locomotive with headlights on at dusk"></div>
  <div class="abs feature-panel" style="left:600px;top:991px;width:600px;height:402px">
    <h2>What We Do</h2>
    <p>The LFC reviews all introduced legislation in the House and Senate. Proposed legislation affecting the rail industry is shared with our members. Final industry positions regarding legislation are then communicated to the legislature. We pursue the same activity with appropriate personnel in the state departments and the legislative rules process.</p>
    <span class="btn">Learn More</span>
  </div>
</section>

<section>
  <div class="abs feature-photo" style="top:1483px;height:513px;background:linear-gradient(100deg,#d7dde4,#8fa2b6 45%,#3f5a3a 70%,#2b3f6a)" role="img" aria-label="Freight train with blue containers rounding a curve"></div>
  <div class="abs feature-panel" style="left:0;top:1540px;width:600px;height:403px;padding-left:87px">
    <h2>WHO WE ARE</h2>
    <p>The Lakeshore Freightways Council (LFC) is a non-profit trade association that represents the interests of freight railroads operating in Michigan. LFC members range in size from large Class 1 interstate carriers to smaller regional carriers and shortline railroads. LFC members account for over 95% of all freight rail moved in Michigan.</p>
    <span class="btn">Learn More</span>
  </div>
</section>

<section>
  <div class="abs feature-photo" style="top:2030px;height:510px;background:linear-gradient(110deg,#24324e,#4a5f80 40%,#b23a2a 55%,#dfe4ea 80%)" role="img" aria-label="Red locomotive plowing through snow at a grade crossing"></div>
  <div class="abs feature-panel" style="left:600px;top:2087px;width:600px;height:400px">
    <h2>How to Join LFC</h2>
    <p>LFC membership is open to any freight railroad with Michigan operations. Please contact the LFC office for membership information.</p>
    <p>Companies which supply goods or services to the railroad industry are eligible for a non-voting Associate Membership. Annual dues are $1,000 per year for supplier members.</p>
    <span class="btn">Meet Our Members</span>
  </div>
</section>

<section>
  <div class="abs newsletter-bg" role="img" aria-label="Dark close view of a locomotive"></div>
  <div class="abs newsletter-box">
    <h2>Join Our Newsletter List</h2>
    <div class="abs field" style="left:30px;width:409px">Your Name</div>
    <div class="abs field" style="left:453px;width:409px">Your Email</div>
    <div class="abs send"><svg width="16" height="16" viewBox="0 0 16 16"><path d="M1 8 L15 1 L11 15 L8 9 Z" fill="#fff"/></svg>Send</div>
  </div>
</section>

<section class="contacts">
  <div class="abs contact-item" style="left:72px">
    <div class="contact-icon"><svg width="36" height="36" viewBox="0 0 36 36"><path d="M9 5 L14 5 L16 12 L12 15 Q16 22 21 24 L24 20 L31 22 L31 27 Q30 32 25 31 Q10 27 5 11 Q5 6 9 5Z" fill="#f08a4b"/></svg></div>
    <p class="big">(555) 014-2210</p>
  </div>
  <div class="abs contact-item" style="left:337px">
    <div class="contact-icon"><svg width="36" height="36" viewBox="0 0 36 36"><path d="M18 3 Q28 3 28 13 Q28 21 18 33 Q8 21 8 13 Q8 3 18 3Z" fill="none" stroke="#f08a4b" stroke-width="3"/><circle cx="18" cy="13" r="4" fill="#f08a4b"/></svg></div>
    <p>410 Harbor Street,<br>Suite 220 Marlow, MI 49001</p>
  </div>
  <div class="abs contact-item" style="left:601px">
    <div class="contact-icon"><svg width="36" height="36" viewBox="0 0 36 36"><rect x="6" y="12" width="24" height="18" rx="2" fill="#f08a4b"/><rect x="11" y="4" width="14" height="10" fill="none" stroke="#f08a4b" stroke-width="2.5"/><rect x="11" y="18" width="14" height="2" fill="#fff"/><rect x="11" y="23" width="14" height="2" fill="#fff"/></svg></div>
    <p class="big">(555) 014-2288</p>
  </div>
  <div class="abs contact-item" style="left:865px">
    <div class="contact-icon"><svg width="36" height="36" viewBox="0 0 36 36"><circle cx="18" cy="18" r="6" fill="none" stroke="#f08a4b" stroke-width="3"/><path d="M24 12 L24 21 Q24 25 28 24 Q32 22 31 17 A13 13 0 1 0 24 29" fill="none" stroke="#f08a4b" stroke-width="3"/></svg></div>
    <p>info@lakeshorefreightways<br>council.com</p>
  </div>
</section>

<footer class="abs about">
  <h2>About Us</h2>
  <p class="abs about-text">I would like to welcome you to the Lakeshore Freightways Council website. Here you will find valuable information on Michigan railroads, including issues and concerns in and around the railroad industry. We are an active and aggressive state railroad association and we look forward to continued success with our partnerships. Please make sure to click on our member railroad company links while you're here. Also, sign up for our newsletter and follow the LFC on our news feed. Thank you and I hope you enjoy your visit to our website.</p>
  <div class="abs badge">
    <div class="badge-shape"></div>
    <p>Click HERE to learn which railroads hire veterans.</p>
  </div>
  <div class="abs feed">
    <h3>Latest Posts</h3>
    <p><span class="av"></span>Glad to welcome members at the spring rail safety forum.</p>
  </div>
</footer>
<div class="abs legal">Copyright © 2017 Lakeshore Freightways Council. All rights reserved. Developed by Brightline Studio.</div>

</body>
</html>
```